Aviation club power point template

Hello designers
we are a small aviation club with about 100 members in germany. we love flying and are looking for a professional power point template for our public relations.
Here is the link to our homepage
https://www.lgk-treblingen.de/
the template should be aviation related and should be about gliders and small powered aircraft.
Here you can find our gliders (you see the right link only in german language)
https://www.lgk-treblingen.de/flying/gliding/
Here you can find our motor planes (Only Falke KX-250) (you see the right link only in German language)
https://www.lgk-treblingen.de/flying/motorflying/
I found a model of the Falke KX-250 motor plane, but in green. We have a red-white painting
http://www.planzumodel.com/wp-content/uploads/Image10-300x198. png
Required foils:
3 welcome (one neutral, one glider, one powered plane)
1-2 agenda
2-3 statistics
2-3 enumerations
2-3 free slides
We look forward to your suggestions and thank you in advance for your work. If you have any questions or need more data. Please write us.
greetings
jorg

```html
<!DOCTYPE html>
<html lang="en">
<head>
<meta charset="utf-8">
<title>LGK Treblingen e.V. – Presentation Template</title>
<link href="https://fonts.googleapis.com/css2?family=Open+Sans:wght@300;400;600;700&display=swap" rel="stylesheet">
<style>
  :root{
    --navy:#26346a;
    --navy-deep:#1f2b5a;
    --backdrop:#4b5f98;
    --blue-mid:#3f67a8;
    --blue-light:#c7d2ee;
    --blue-pale:#e4eaf7;
    --sky:#d9ecf3;
    --text-grey:#6b6f7a;
    --white:#ffffff;
  }
  *{box-sizing:border-box;margin:0;padding:0}
  html,body{width:1200px;height:3000px;overflow:hidden}
  body{background:var(--backdrop);font-family:"Open Sans",Arial,sans-serif;position:relative;color:var(--navy)}

  .hero{position:absolute;left:0;top:0;width:1200px;height:620px;background:var(--navy)}
  .hero-brand{position:absolute;left:50%;top:50%;transform:translate(-50%,-50%);display:flex;align-items:center;gap:36px}
  .hero-ring{width:200px;height:200px;border:6px solid var(--white);border-radius:50%}
  .hero-name{color:var(--white);font-size:46px;font-weight:600;letter-spacing:1px}

  .slide{position:absolute;width:540px;height:304px;background:var(--white);overflow:hidden}
  .col-left{left:48px}.col-right{left:612px}
  .row-1{top:660px}.row-2{top:990px}.row-3{top:1320px}.row-4{top:1650px}
  .row-5{top:1980px}.row-6{top:2310px}.row-7{top:2640px}

  .slide-title{position:absolute;left:26px;top:18px;font-size:22px;font-weight:400;color:var(--navy)}
  .corner-mark{position:absolute;right:14px;top:12px;display:flex;align-items:center;gap:4px;font-size:8px;font-weight:600;color:var(--navy)}
  .corner-mark span{width:16px;height:16px;border:1.5px solid var(--navy);border-radius:50%}
  .page-no{position:absolute;left:12px;bottom:10px;width:16px;height:16px;border-radius:50%;background:var(--navy);color:var(--white);font-size:8px;display:flex;align-items:center;justify-content:center}
  .body-copy{font-size:7.5px;line-height:1.6;color:var(--text-grey)}
  .body-copy p+p{margin-top:8px}

  .photo{position:absolute}
  .photo-aerial{background:linear-gradient(180deg,#8fa9c4 0%,#5d7a5a 45%,#3f5a3c 100%)}
  .photo-glider-sky{background:linear-gradient(180deg,#b9d3ea 0%,#dfe9f2 55%,#6d8460 100%)}
  .photo-red-plane{background:linear-gradient(135deg,#e4f1f6 0%,#cfe4ee 60%,#c9d8e6 100%)}
  .photo-field{background:linear-gradient(180deg,#b8cde0 0%,#d7e2ea 50%,#7e9470 100%)}

  .cover-brand{position:absolute;left:50%;top:50%;transform:translate(-50%,-50%);display:flex;align-items:center;gap:12px}
  .cover-brand span{width:70px;height:70px;border:3px solid var(--white);border-radius:50%}
  .cover-brand b{color:var(--white);font-size:18px;font-weight:600}
  .cover-caption{position:absolute;left:14px;bottom:10px;color:var(--white);font-size:8px}
  .shape-layer{position:absolute;left:0;top:0}

  .agenda-panel{position:absolute;left:0;top:0;width:200px;height:304px;background:var(--navy)}
  .agenda-panel h2{position:absolute;left:22px;bottom:30px;color:var(--white);font-weight:400;font-size:22px}
  .agenda-list{position:absolute;left:232px;top:38px;list-style:none}
  .agenda-list li{display:flex;align-items:baseline;gap:10px;margin-bottom:22px;font-size:12px;color:var(--navy)}
  .agenda-list li::before{content:"";width:7px;height:7px;border-radius:50%;background:var(--navy);flex:none;transform:translateY(-1px)}
  .agenda-list small{font-size:7px;color:var(--text-grey)}

  .agenda-tag{position:absolute;left:26px;top:22px;width:150px;height:40px;background:var(--navy);color:var(--white);font-size:16px;display:flex;align-items:center;padding-left:16px}
  .agenda-grid{position:absolute;left:26px;top:90px;display:grid;grid-template-columns:230px 230px;column-gap:30px;row-gap:16px;list-style:none}
  .agenda-grid li{display:flex;align-items:center;gap:10px;font-size:11px;color:var(--navy);border-bottom:1px solid var(--blue-light);padding-bottom:6px}
  .agenda-grid li::before{content:"";width:9px;height:9px;border-radius:50%;background:var(--navy)}

  .stat{position:absolute;display:flex;gap:14px;align-items:center}
  .stat-value{font-size:22px;color:var(--navy);font-weight:400;line-height:1}
  .stat-label{font-size:9px;color:var(--navy)}
  .stat-note{font-size:6.5px;color:var(--text-grey);width:90px}

  .big-box{position:absolute;width:150px;height:44px;display:flex;align-items:center;justify-content:center;font-size:24px;color:var(--navy)}
  .big-box.filled{background:var(--blue-light)}
  .big-label{position:absolute;width:150px;text-align:center;font-size:9px;color:var(--navy)}

  .chart-copy{position:absolute;left:300px;top:80px;width:210px}
  .ring-item{position:absolute;top:80px;width:110px;text-align:center}
  .ring-item h4{font-size:9px;font-weight:600;color:var(--navy);margin-top:10px}
  .ring-item p{font-size:6.5px;color:var(--text-grey);margin-top:4px}

  .thumb-card{position:absolute;top:80px;width:150px}
  .thumb-card .thumb{height:92px}
  .thumb-card p{font-size:7px;color:var(--text-grey);text-align:center;margin-top:8px}

  .thanks-text{position:absolute;left:40px;top:100px;color:var(--white);font-size:40px;font-weight:600;line-height:1.15;letter-spacing:2px}
</style>
</head>
<body>

<header class="hero">
  <div class="hero-brand">
    <div class="hero-ring"></div>
    <div class="hero-name">LGK Treblingen e.V.</div>
  </div>
</header>

<!-- Row 1 -->
<section class="slide col-left row-1">
  <div class="photo photo-aerial" style="left:0;top:0;width:540px;height:304px" role="img" aria-label="Aerial view of green hills and forest below the airfield"></div>
  <div class="cover-brand"><span></span><b>LGK Treblingen e.V.</b></div>
  <div class="cover-caption">LGK Treblingen e.V.</div>
</section>

<section class="slide col-right row-1">
  <div class="photo photo-glider-sky" style="left:0;top:0;width:540px;height:304px" role="img" aria-label="White glider flying over a green valley"></div>
  <svg class="shape-layer" width="540" height="304" viewBox="0 0 540 304">
    <polygon points="300,0 540,0 540,304 430,304" fill="#26346a" opacity="0.9"/>
    <polygon points="250,0 320,0 450,304 400,304" fill="#3f67a8" opacity="0.55"/>
  </svg>
</section>

<!-- Row 2 -->
<section class="slide col-left row-2">
  <div class="photo photo-red-plane" style="left:0;top:0;width:540px;height:304px" role="img" aria-label="Red and white motor glider in flight against a pale sky"></div>
  <svg class="shape-layer" width="540" height="304" viewBox="0 0 540 304">
    <polygon points="270,0 540,0 540,304 410,304" fill="#26346a"/>
    <polygon points="270,0 330,0 470,304 410,304" fill="#3f67a8" opacity="0.6"/>
  </svg>
</section>

<section class="slide col-right row-2">
  <div class="agenda-panel"><h2>Agenda</h2></div>
  <ul class="agenda-list">
    <li>Introduction <small>Short note here</small></li>
    <li>About our team <small>Short note here</small></li>
    <li>Company history <small>Short note here</small></li>
    <li>Who we are <small>Short note here</small></li>
    <li>Our pricing <small>Short note here</small></li>
  </ul>
  <div class="corner-mark"><span></span></div>
</section>

<!-- Row 3 -->
<section class="slide col-left row-3">
  <div class="agenda-tag">AGENDA</div>
  <ul class="agenda-grid">
    <li>Introduction</li><li>Introduction</li>
    <li>Introduction</li><li>Introduction</li>
    <li>Introduction</li><li>Introduction</li>
    <li>Introduction</li><li>Introduction</li>
  </ul>
  <div class="corner-mark"><span></span></div>
  <div class="page-no">3</div>
</section>

<section class="slide col-right row-3">
  <h3 class="slide-title">Text with Numbers</h3>
  <div class="stat" style="left:40px;top:78px">
    <div><div class="stat-value">28%</div><div class="stat-label">Some Text</div><div class="stat-note">Short text about this figure</div></div>
    <svg width="50" height="50" viewBox="0 0 50 50"><path d="M25 0 A25 25 0 0 1 25 50 Z" fill="#c7d2ee"/></svg>
  </div>
  <div class="stat" style="left:290px;top:78px">
    <svg width="50" height="50" viewBox="0 0 50 50"><path d="M25 0 A25 25 0 0 0 25 50 Z" fill="#c7d2ee"/></svg>
    <div><div class="stat-value">90%</div><div class="stat-label">Some Text</div><div class="stat-note">Short text about this figure</div></div>
  </div>
  <div class="stat" style="left:150px;top:180px">
    <svg width="50" height="50" viewBox="0 0 50 50"><path d="M25 0 A25 25 0 0 0 25 50 Z" fill="#26346a"/></svg>
    <div><div class="stat-value">60%</div><div class="stat-label">Some Text</div><div class="stat-note">Short text about this figure</div></div>
  </div>
  <div class="stat" style="left:370px;top:180px">
    <div><div class="stat-value">80%</div><div class="stat-label">Some Text</div><div class="stat-note">Short text about this figure</div></div>
    <svg width="50" height="50" viewBox="0 0 50 50"><path d="M25 0 A25 25 0 0 1 25 50 Z" fill="#26346a"/></svg>
  </div>
  <div class="corner-mark"><span></span></div>
  <div class="page-no">4</div>
</section>

<!-- Row 4 -->
<section class="slide col-left row-4">
  <h3 class="slide-title">Big Numbers</h3>
  <div class="big-box filled" style="left:60px;top:80px">300,000</div>
  <div class="big-label" style="left:60px;top:130px">Big numbers</div>
  <div class="big-box" style="left:300px;top:80px">300,000</div>
  <div class="big-label" style="left:300px;top:130px">Big numbers</div>
  <div class="big-box" style="left:60px;top:180px">300,000</div>
  <div class="big-label" style="left:60px;top:230px">Big numbers</div>
  <div class="big-box filled" style="left:300px;top:180px">300,000</div>
  <div class="big-label" style="left:300px;top:230px">Big numbers</div>
  <div class="corner-mark"><span></span></div>
  <div class="page-no">5</div>
</section>

<section class="slide col-right row-4">
  <h3 class="slide-title">Bar Charts</h3>
  <svg class="shape-layer" width="540" height="304" viewBox="0 0 540 304">
    <line x1="40" y1="250" x2="270" y2="250" stroke="#c7d2ee" stroke-width="1"/>
    <rect x="60" y="130" width="24" height="120" fill="#26346a"/>
    <rect x="90" y="100" width="24" height="150" fill="#3f67a8"/>
    <rect x="120" y="160" width="24" height="90" fill="#c7d2ee"/>
    <rect x="170" y="150" width="24" height="100" fill="#26346a"/>
    <rect x="200" y="190" width="24" height="60" fill="#3f67a8"/>
    <rect x="230" y="110" width="24" height="140" fill="#c7d2ee"/>
    <g font-family="Open Sans, sans-serif" font-size="7" fill="#26346a" text-anchor="middle">
      <text x="72" y="126">40</text><text x="102" y="96">50</text><text x="132" y="156">30</text>
      <text x="182" y="146">33</text><text x="212" y="186">20</text><text x="242" y="106">47</text>
      <text x="102" y="264">Product 1</text><text x="212" y="264">Product 2</text>
    </g>
  </svg>
  <div class="chart-copy body-copy">
    <p>Our fleet flew more hours this season than ever before, thanks to new members and great weather.</p>
    <p>Gliders and the motor glider shared the load across the whole year.</p>
  </div>
  <div class="corner-mark"><span></span></div>
  <div class="page-no">6</div>
</section>

<!-- Row 5 -->
<section class="slide col-left row-5">
  <h3 class="slide-title">Pie Charts</h3>
  <div class="ring-item" style="left:20px">
    <svg width="64" height="64" viewBox="0 0 64 64"><circle cx="32" cy="32" r="26" fill="none" stroke="#e4eaf7" stroke-width="6"/><circle cx="32" cy="32" r="26" fill="none" stroke="#26346a" stroke-width="6" stroke-dasharray="116 163.4" transform="rotate(-90 32 32)"/><text x="32" y="35" text-anchor="middle" font-family="Open Sans, sans-serif" font-size="10" fill="#26346a">71</text></svg>
    <h4>Project name</h4><p>Short line of detail</p>
  </div>
  <div class="ring-item" style="left:148px">
    <svg width="64" height="64" viewBox="0 0 64 64"><circle cx="32" cy="32" r="26" fill="none" stroke="#e4eaf7" stroke-width="6"/><circle cx="32" cy="32" r="26" fill="none" stroke="#26346a" stroke-width="6" stroke-dasharray="85 163.4" transform="rotate(-90 32 32)"/><text x="32" y="35" text-anchor="middle" font-family="Open Sans, sans-serif" font-size="10" fill="#26346a">52</text></svg>
    <h4>Project name</h4><p>Short line of detail</p>
  </div>
  <div class="ring-item" style="left:276px">
    <svg width="64" height="64" viewBox="0 0 64 64"><circle cx="32" cy="32" r="26" fill="none" stroke="#e4eaf7" stroke-width="6"/><circle cx="32" cy="32" r="26" fill="none" stroke="#26346a" stroke-width="6" stroke-dasharray="137 163.4" transform="rotate(-90 32 32)"/><text x="32" y="35" text-anchor="middle" font-family="Open Sans, sans-serif" font-size="10" fill="#26346a">84</text></svg>
    <h4>Project name</h4><p>Short line of detail</p>
  </div>
  <div class="ring-item" style="left:404px">
    <svg width="64" height="64" viewBox="0 0 64 64"><circle cx="32" cy="32" r="26" fill="none" stroke="#e4eaf7" stroke-width="6"/><circle cx="32" cy="32" r="26" fill="none" stroke="#26346a" stroke-width="6" stroke-dasharray="147 163.4" transform="rotate(-90 32 32)"/><text x="32" y="35" text-anchor="middle" font-family="Open Sans, sans-serif" font-size="10" fill="#26346a">90</text></svg>
    <h4>Project name</h4><p>Short line of detail</p>
  </div>
  <div class="corner-mark"><span></span></div>
  <div class="page-no">7</div>
</section>

<section class="slide col-right row-5">
  <h3 class="slide-title">Images with text</h3>
  <div class="thumb-card" style="left:22px">
    <div class="thumb photo-glider-sky" role="img" aria-label="Glider landing on the grass strip"></div>
    <p>Caption text here</p>
  </div>
  <div class="thumb-card" style="left:195px">
    <div class="thumb photo-field" role="img" aria-label="Motor glider parked on the airfield"></div>
    <p>Caption text here</p>
  </div>
  <div class="thumb-card" style="left:368px">
    <div class="thumb photo-aerial" role="img" aria-label="Glider above the valley"></div>
    <p>Caption text here</p>
  </div>
  <div class="corner-mark"><span></span></div>
  <div class="page-no">8</div>
</section>

<!-- Row 6 -->
<section class="slide col-left row-6">
  <h3 class="slide-title">Text only</h3>
  <div class="body-copy" style="position:absolute;left:26px;top:70px;width:300px">
    <p>Our club meets every weekend at the airfield, where members of all ages learn to fly gliders and our motor glider under the guidance of experienced instructors.</p>
    <p>New pilots start with a trial flight and a short briefing on the ground.</p>
    <p>Between flights we maintain the aircraft together, plan cross-country tasks and share the joy of flying with guests and families.</p>
  </div>
  <div class="corner-mark"><span></span></div>
  <div class="page-no">9</div>
</section>

<section class="slide col-right row-6">
  <h3 class="slide-title">Text with image</h3>
  <div class="body-copy" style="position:absolute;left:26px;top:70px;width:230px">
    <p>Gliding is quiet, efficient flight that uses rising air to stay aloft for hours and cover long distances.</p>
    <p>Our instructors guide every student from the first launch to the first solo.</p>
  </div>
  <div class="photo photo-glider-sky" style="left:290px;top:40px;width:220px;height:230px" role="img" aria-label="White glider banking over green hills"></div>
  <div class="page-no">10</div>
</section>

<!-- Row 7 -->
<section class="slide col-left row-7">
  <h3 class="slide-title">Text with image</h3>
  <div class="photo photo-glider-sky" style="left:26px;top:60px;width:220px;height:215px" role="img" aria-label="Glider wing over a landscape of fields"></div>
  <div class="body-copy" style="position:absolute;left:270px;top:70px;width:240px">
    <p>The motor glider lets us reach distant thermals and offers relaxed sightseeing flights over the hills.</p>
    <p>Guests are welcome to join us for a flight on open days.</p>
  </div>
  <div class="corner-mark"><span></span></div>
  <div class="page-no">11</div>
</section>

<section class="slide col-right row-7">
  <div class="photo photo-red-plane" style="left:0;top:0;width:540px;height:304px" role="img" aria-label="Red and white motor glider flying in a clear sky"></div>
  <svg class="shape-layer" width="540" height="304" viewBox="0 0 540 304">
    <polygon points="0,0 260,0 190,304 0,304" fill="#26346a"/>
    <polygon points="260,0 300,0 230,304 190,304" fill="#3f67a8" opacity="0.6"/>
  </svg>
  <div class="thanks-text">THANK<br>YOU</div>
</section>

</body>
</html>
```